Design blogshop facebook and logo

Design logo and blog shop facebook design.
Reference https://www.pagevault.example/Pellu-Vandirk-527061983314702/?ref=ts&fref=ts
Want a more trendy elegant and fashionable design for the logo and facebook

Industry/Entity Type

Shop

Colors
ffffff
ec1f27
f68d4d

```html
<!DOCTYPE html>
<html lang="en">
<head>
<meta charset="utf-8">
<title>Pellu Vandirk – Cover and Badge</title>
<link rel="stylesheet" href="https://fonts.googleapis.com/css2?family=Almendra:wght@700&family=Open+Sans:wght@600&display=swap">
<style>
  :root {
    --canvas: #ffffff;
    --ink: #000000;
    --violet: #b51dfb;
    --violet-soft: #d98cff;
    --mist: #a7a9ac;
    --navy: #0c1550;
    --paper: #ffffff;
    --frame: #d4d4d4;
    --dress-dark: #1c1f2e;
    --skin: #c79a7c;
  }
  * { margin: 0; padding: 0; box-sizing: border-box; }
  html, body {
    width: 1200px;
    height: 647px;
    overflow: hidden;
    background: var(--canvas);
  }
  .canvas {
    position: relative;
    width: 1200px;
    height: 647px;
  }
  .cover {
    position: absolute;
    left: 58px;
    top: 60px;
    width: 1072px;
    height: 395px;
    overflow: hidden;
    box-shadow: 0 0 3px rgba(0,0,0,0.35);
  }
  .cover-shapes {
    position: absolute;
    inset: 0;
    width: 100%;
    height: 100%;
  }
  .cover-title {
    position: absolute;
    font-family: "Almendra", serif;
    font-weight: 700;
    line-height: 1;
    white-space: nowrap;
  }
  .cover-title--first {
    left: 70px;
    top: 92px;
    font-size: 92px;
    color: var(--paper);
  }
  .cover-title--second {
    left: 380px;
    top: 150px;
    font-size: 76px;
    color: var(--violet);
  }
  .badge {
    position: absolute;
    left: 148px;
    top: 407px;
    width: 208px;
    height: 197px;
    background: var(--ink);
    border: 3px solid var(--frame);
    border-radius: 30px;
    display: flex;
    flex-direction: column;
    align-items: center;
    justify-content: flex-end;
    padding-bottom: 22px;
    gap: 18px;
  }
  .badge-mark {
    width: 96px;
    height: 96px;
    background: var(--violet);
  }
  .badge-name {
    font-family: "Open Sans", sans-serif;
    font-weight: 600;
    font-size: 22px;
    line-height: 1;
    color: var(--paper);
    white-space: nowrap;
  }
</style>
</head>
<body>
  <main class="canvas">
    <section class="cover">
      <svg class="cover-shapes" viewBox="0 0 1072 395" preserveAspectRatio="none">
        <defs>
          <radialGradient id="look-striped" cx="0.5" cy="0.55" r="0.55">
            <stop offset="0" stop-color="var(--dress-dark)" stop-opacity="0.75"/>
            <stop offset="0.45" stop-color="var(--skin)" stop-opacity="0.35"/>
            <stop offset="1" stop-color="var(--mist)" stop-opacity="0"/>
          </radialGradient>
          <radialGradient id="look-floral" cx="0.5" cy="0.55" r="0.55">
            <stop offset="0" stop-color="#d9d9de" stop-opacity="0.7"/>
            <stop offset="0.45" stop-color="var(--skin)" stop-opacity="0.3"/>
            <stop offset="1" stop-color="var(--navy)" stop-opacity="0"/>
          </radialGradient>
          <radialGradient id="look-sheath" cx="0.55" cy="0.55" r="0.55">
            <stop offset="0" stop-color="var(--dress-dark)" stop-opacity="0.7"/>
            <stop offset="0.45" stop-color="var(--skin)" stop-opacity="0.35"/>
            <stop offset="1" stop-color="var(--paper)" stop-opacity="0"/>
          </radialGradient>
        </defs>
        <rect class="base" x="0" y="0" width="700" height="395" fill="var(--ink)"/>
        <polygon class="band-violet" points="130,0 442,0 192,395 0,395 0,180" fill="var(--violet)"/>
        <polygon class="panel-light" points="462,15 700,15 700,280 232,280" fill="var(--paper)"/>
        <polygon class="band-glow" points="420,0 478,0 236,340 188,340" fill="var(--violet-soft)" opacity="0.85"/>
        <g role="img" aria-label="Model wearing a striped sleeveless dress holding a quilted handbag">
          <polygon points="692,0 842,0 792,395 652,395" fill="var(--mist)"/>
          <polygon points="692,0 842,0 792,395 652,395" fill="url(#look-striped)"/>
        </g>
        <g role="img" aria-label="Model wearing a black and white floral dress carrying a tote">
          <polygon points="842,0 972,0 927,395 792,395" fill="var(--navy)"/>
          <polygon points="842,0 972,0 927,395 792,395" fill="url(#look-floral)"/>
        </g>
        <g role="img" aria-label="Model wearing a navy sheath dress with white panel lines holding a clutch">
          <polygon points="972,0 1072,0 1072,395 927,395" fill="var(--paper)"/>
          <polygon points="972,0 1072,0 1072,395 927,395" fill="url(#look-sheath)"/>
        </g>
      </svg>
      <h1 class="cover-title cover-title--first">Pellu</h1>
      <p class="cover-title cover-title--second">Vandirk</p>
    </section>
    <aside class="badge">
      <span class="badge-mark"></span>
      <span class="badge-name">Pellu Vandirk</span>
    </aside>
  </main>
</body>
</html>
```